Company director needs a business card design

I am a semi-retired former senior finance executive who sits on a number of public and private company boards and do some consulting work. I work largely with emerging businesses but deal regularly with top end of town lawyers, bankers etc. I need a thoughtful but relatively conservative design which would also resonate with my younger client base. Some colour would be good. Information limited to name, address, office tel, mobile and email.

Industry/Entity Type

Finance

```html
<!DOCTYPE html>
<html lang="en">
<head>
<meta charset="utf-8">
<title>Martin Calloway – Business Card</title>
<link rel="stylesheet" href="https://fonts.googleapis.com/css2?family=Roboto:wght@300;400;700&display=swap">
<style>
  :root {
    --backdrop: #5ccfbd;
    --card: #2a2927;
    --card-edge: #1f1e1c;
    --text-strong: #ffffff;
    --text-soft: #b9b8b4;
    --text-body: #d6d5d1;
    --green-dark: #4e9a1f;
    --green-mid: #64b52a;
    --green-light: #8ccf4a;
    --icon: #ffffff;
  }
  html, body {
    margin: 0;
    padding: 0;
    width: 1200px;
    height: 836px;
    overflow: hidden;
    background: var(--backdrop);
  }
  .canvas {
    position: relative;
    width: 1200px;
    height: 836px;
  }
  .business-card {
    position: absolute;
    left: 150px;
    top: 148px;
    width: 900px;
    height: 540px;
    background: var(--card);
    border-radius: 6px;
    box-shadow: 0 18px 40px rgba(0, 0, 0, 0.25);
    font-family: "Roboto", Arial, sans-serif;
    overflow: hidden;
  }
  .holder-name {
    position: absolute;
    left: 70px;
    top: 150px;
    margin: 0;
    font-size: 64px;
    line-height: 1;
    letter-spacing: -0.5px;
    white-space: nowrap;
  }
  .holder-name .given {
    font-weight: 700;
    color: var(--text-strong);
  }
  .holder-name .family {
    font-weight: 300;
    color: var(--text-soft);
  }
  .contact-strip {
    position: absolute;
    left: 0;
    top: 0;
  }
  .contact-details {
    position: absolute;
    left: 392px;
    top: 256px;
    margin: 0;
    font-style: normal;
    font-size: 22px;
    line-height: 30px;
    font-weight: 400;
    color: var(--text-body);
  }
  .contact-details p {
    margin: 0;
  }
  .contact-details .address { height: 80px; }
  .contact-details .phones { height: 80px; }
</style>
</head>
<body>
<main class="canvas">
  <section class="business-card">
    <h1 class="holder-name"><span class="given">Martin</span> <span class="family">Calloway</span></h1>

    <svg class="contact-strip" width="900" height="540" viewBox="0 0 900 540" aria-hidden="true">
      <polygon points="316,262 364,244 364,332 316,332" fill="var(--green-light)"/>
      <rect x="316" y="332" width="48" height="74" fill="var(--green-mid)"/>
      <rect x="316" y="406" width="48" height="66" fill="var(--green-dark)"/>

      <!-- home -->
      <g fill="var(--icon)">
        <polygon points="340,277 328,288 332,288 332,299 337,299 337,292 343,292 343,299 348,299 348,288 352,288"/>
      </g>
      <!-- phone handset -->
      <g fill="var(--icon)">
        <path d="M331,360 q0,-4 4,-4 h10 q4,0 4,4 v2 h-5 v-2 h-8 v2 h-5 z"/>
        <rect x="331" y="364" width="18" height="12" rx="2"/>
      </g>
      <!-- screen -->
      <g fill="none" stroke="var(--icon)" stroke-width="2.5">
        <rect x="331" y="430" width="18" height="14" rx="1"/>
      </g>
      <rect x="336" y="446" width="8" height="2.5" fill="var(--icon)"/>
    </svg>

    <address class="contact-details">
      <div class="address">
        <p>18 Kellan Street</p>
        <p>Seabrook NSW 2110</p>
      </div>
      <div class="phones">
        <p>02 9000 4815</p>
        <p>0400 217 639</p>
      </div>
      <p class="email">martin_calloway@mailbox.net.au</p>
    </address>
  </section>
</main>
</body>
</html>
```